Virtualization software: PowerPoint, business cards

We're a young, small, dynamic application virtualization company: www.vorlint.com
We need a PowerPoint template + business cards. PDF background will be a plus.
This is mostly for enterprise clients.
Clean, professional, and most of all - following our website's colors.

Reason: Busy weekend; we'll need some more time to provide feedback & choose.

Corporate clients & investors.

Business

• Clean, professional, and following our website's look: www.vorlint.com

```html
<!DOCTYPE html>
<html lang="en">
<head>
<meta charset="utf-8">
<title>Vorlint business card</title>
<link rel="stylesheet" href="https://fonts.googleapis.com/css2?family=Arimo:wght@400;700&display=swap">
<style>
  :root {
    --page-bg: #e9e7e5;
    --card-dark: #1f1d1e;
    --card-mid: #3b393a;
    --text-light: #ffffff;
    --text-soft: #e4e4e4;
    --tag-bg: #4a4849;
    --band-light: #f6f6f6;
    --band-grey: #b9b9b9;
    --url-dark: #555455;
    --url-faint: #4a4849;
  }
  * { margin: 0; padding: 0; box-sizing: border-box; }
  html, body { width: 1200px; height: 900px; overflow: hidden; }
  body {
    background: var(--page-bg);
    font-family: "Arimo", Arial, sans-serif;
    position: relative;
  }
  .card {
    position: absolute;
    top: 306px;
    width: 504px;
    height: 288px;
    border-radius: 16px;
    overflow: hidden;
    background: radial-gradient(ellipse at 58% 45%, var(--card-mid) 0%, var(--card-dark) 70%);
    box-shadow: 0 6px 16px rgba(0,0,0,0.25);
  }
  .card-front { left: 64px; }
  .card-back { left: 632px; }

  .name-tag {
    position: absolute;
    left: 0; top: 82px;
    width: 190px; height: 26px;
    background: linear-gradient(90deg, #2e2c2d 0%, var(--tag-bg) 60%, #555354 100%);
    border-radius: 0 13px 13px 0;
  }
  .person-name {
    position: absolute;
    left: 35px; top: 87px;
    font-size: 15px; font-weight: 700;
    color: var(--text-light);
  }
  .person-role {
    position: absolute;
    left: 35px; top: 120px;
    font-size: 14px;
    color: var(--text-soft);
  }
  .company-name {
    position: absolute;
    left: 38px; top: 157px;
    font-size: 12px;
    color: var(--text-soft);
  }
  .contact {
    position: absolute;
    left: 34px;
    display: flex; align-items: center; gap: 7px;
    font-size: 12.5px;
    color: var(--text-soft);
  }
  .contact svg { width: 13px; height: 11px; fill: var(--text-light); flex: none; }
  .contact-phone { top: 190px; }
  .contact-mail { top: 208px; }
  .contact b { font-weight: 700; color: var(--text-light); }

  .wordmark {
    position: absolute;
    color: var(--text-light);
    font-weight: 400;
    letter-spacing: 0.06em;
    line-height: 1;
  }
  .card-front .wordmark { left: 226px; top: 118px; font-size: 38px; }
  .card-back .wordmark { left: 0; right: 0; top: 114px; text-align: center; font-size: 48px; }

  .url-band {
    position: absolute;
    left: 0; bottom: 0;
    width: 100%; height: 35px;
    background: linear-gradient(90deg, var(--band-light) 0%, #e2e2e2 55%, var(--band-grey) 100%);
  }
  .url {
    position: absolute;
    font-size: 15px;
    letter-spacing: 0.22em;
  }
  .card-front .url { right: 48px; bottom: 9px; color: var(--url-dark); }
  .card-back .url { left: 0; right: 0; text-align: center; top: 260px; color: var(--url-faint); }
</style>
</head>
<body>
  <section class="card card-front">
    <div class="name-tag"></div>
    <p class="person-name">Daniel Reese Hartwell</p>
    <p class="person-role">President</p>
    <p class="company-name">Vorlint</p>
    <p class="contact contact-phone">
      <svg viewBox="0 0 13 11" aria-hidden="true"><path d="M1 4.2C1 2 4 1 6.5 1S12 2 12 4.2L9.6 4.8 9 3.4C7.5 3 5.5 3 4 3.4L3.4 4.8Z"/><path d="M3.2 5.4h6.6l1.4 4.6H1.8z"/></svg>
      <span><b>(DK)</b> (705) 555-0142</span>
    </p>
    <p class="contact contact-mail">
      <svg viewBox="0 0 13 11" aria-hidden="true"><path d="M0.5 1.5h12v8h-12zM1.7 2.7v.3L6.5 6l4.8-3v-.3zM1.7 4.4v4h9.6v-4L6.5 7.4z" fill-rule="evenodd"/></svg>
      <span>info@vorlint.com</span>
    </p>
    <p class="wordmark">VORLINT</p>
    <div class="url-band"></div>
    <p class="url">www.vorlint.com</p>
  </section>

  <section class="card card-back">
    <p class="wordmark">VORLINT</p>
    <p class="url">www.vorlint.com</p>
  </section>
</body>
</html>
```